International Freight Forwarder need a business card

We need a logo design for a freight forwarding company . We are active in Sea Transportation, Truck transportation, and Air Transportation, The design should be have normal dimensions of a card and should not have cuts and holes in its design (printed design is required - lamination accepted)

The said company is agent and sales representative of 2 other Shipping companies (whose logos, name, and website should also be mentioned on the card)

Industry/Entity Type

Logistics

Contact Information for Business Card

Address is "No.7, 2nd Sarv Baghestan-e-Nouri, Tehran, IR
Tel number is +98 21 66394512
Fax number is +98 21 66395830
E-Mail address is info@roshanbarsaz.com
Website is www.roshanbarsaz.com

Open Layer Logos attached as well

Colors
33a6d7
0292cd
0255a3
3276b5
85abd2
85cae6
cee9f5
d5e2ee
ffffff

Requirements
Must have
• Main logo of Roshan Barsaz
• Logo of TQM Shipping Line
• London, United Kingdom
• tqmline.com
• Logo of Calm Reef Shipping
• Dubai, United Arab Emirates
• crsuae.com
• We require OPEN layer file to be submitted to us upon project selection.
Should not have
• Weird Designs such as cuts to the shape or holes in design.

```html
<!DOCTYPE html>
<html lang="en">
<head>
<meta charset="utf-8">
<title>Roshan Barsaz – Business Card</title>
<link rel="stylesheet" href="https://fonts.googleapis.com/css2?family=Open+Sans:wght@400;600;700&display=swap">
<style>
  :root {
    --page-bg: #e6e9ee;
    --card-white: #ffffff;
    --partner-blue: #3a86c4;
    --contact-blue: #2b4f97;
    --stripe-light: #85cae6;
    --stripe-mid: #3276b5;
    --brand-blue: #0255a3;
    --ring-grey: #b9bec6;
    --text-white: #ffffff;
  }
  * { box-sizing: border-box; margin: 0; padding: 0; }
  html, body { width: 1200px; height: 900px; overflow: hidden; }
  body {
    background: var(--page-bg);
    font-family: "Open Sans", Arial, sans-serif;
    position: relative;
  }
  .card {
    position: absolute;
    width: 700px;
    height: 400px;
    background: var(--card-white);
    box-shadow: 0 10px 28px rgba(20, 30, 50, 0.22);
    overflow: hidden;
  }
  .card--partners { left: 150px; top: 35px; }
  .card--contact  { left: 350px; top: 465px; }
  .card-shapes { position: absolute; inset: 0; }

  .brand-mark {
    position: absolute;
    display: flex;
    flex-direction: column;
    align-items: center;
    gap: 18px;
  }
  .brand-ring {
    width: 130px; height: 130px;
    border-radius: 50%;
    border: 4px solid var(--ring-grey);
  }
  .brand-name {
    color: var(--brand-blue);
    font-weight: 700;
    font-size: 19px;
    line-height: 1.2;
    text-align: center;
  }
  .card--partners .brand-mark { left: 40px; top: 85px; width: 230px; }
  .card--contact .brand-mark { left: 395px; top: 70px; width: 270px; }

  .partners {
    position: absolute;
    left: 380px; top: 30px; width: 280px;
    color: var(--text-white);
    text-align: center;
    font-size: 15px;
    line-height: 1.3;
  }
  .partner + .partner { margin-top: 30px; }
  .partner-name {
    display: flex; align-items: center; justify-content: center;
    gap: 10px;
    font-weight: 700;
    font-size: 16px;
    margin-bottom: 8px;
  }
  .partner-dot {
    width: 26px; height: 26px; border-radius: 50%;
    background: var(--text-white);
    flex: none;
  }

  .contact {
    position: absolute;
    left: 55px; top: 95px; width: 290px;
    color: var(--text-white);
  }
  .person-name { font-weight: 700; font-size: 19px; letter-spacing: 0.5px; }
  .person-role { font-size: 17px; margin-bottom: 22px; }
  .address { font-size: 15px; line-height: 1.4; margin-bottom: 14px; }
  .contact-list { list-style: none; font-size: 15px; }
  .contact-list li { display: flex; align-items: center; gap: 12px; line-height: 1.6; }
  .contact-list svg { width: 16px; height: 16px; flex: none; }
</style>
</head>
<body>

<section class="card card--partners">
  <svg class="card-shapes" viewBox="0 0 700 400" aria-hidden="true">
    <polygon points="318,0 700,0 700,400 372,400" fill="var(--partner-blue)"/>
    <polygon points="306,0 312,0 366,400 360,400" fill="var(--stripe-mid)"/>
  </svg>
  <div class="brand-mark">
    <div class="brand-ring"></div>
    <p class="brand-name">Roshan Barsaz<br>International<br>Transport.Co L.L.c</p>
  </div>
  <div class="partners">
    <div class="partner">
      <p class="partner-name"><span class="partner-dot"></span>TQM Shipping Line Ltd</p>
      <p>TQM Shipping Line London</p>
      <p>United Kingdom</p>
      <p>tqmline.com</p>
    </div>
    <div class="partner">
      <p class="partner-name"><span class="partner-dot"></span>Calm Reef Shipping LLC</p>
      <p>Calm Reef ShippingDubai</p>
      <p>United Arab Emirates</p>
      <p>crsuae.com</p>
    </div>
  </div>
</section>

<section class="card card--contact">
  <svg class="card-shapes" viewBox="0 0 700 400" aria-hidden="true">
    <polygon points="0,0 330,0 372,400 0,400" fill="var(--contact-blue)"/>
    <polygon points="336,0 342,0 384,400 378,400" fill="var(--stripe-light)"/>
  </svg>
  <div class="contact">
    <p class="person-name">ARASH KARIMI</p>
    <p class="person-role">CEO/FOUNDER</p>
    <p class="address">No.7, 2nd Sarv<br>Baghestan-e-Nouri, Tehran, IR</p>
    <ul class="contact-list">
      <li>
        <svg viewBox="0 0 16 16" aria-label="Phone"><path fill="#fff" d="M3 1h3l1 4-2 1a9 9 0 0 0 5 5l1-2 4 1v3a2 2 0 0 1-2 2A13 13 0 0 1 1 3a2 2 0 0 1 2-2z"/></svg>
        +98 21 66394512
      </li>
      <li>
        <svg viewBox="0 0 16 16" aria-label="Fax"><rect x="4" y="1" width="8" height="5" fill="#fff"/><rect x="1" y="6" width="14" height="6" rx="1" fill="#fff"/><rect x="4" y="10" width="8" height="5" fill="#fff" stroke="var(--contact-blue)"/></svg>
        +98 21 66395830
      </li>
      <li>
        <svg viewBox="0 0 16 16" aria-label="Email"><rect x="1" y="3" width="14" height="10" rx="1" fill="#fff"/><path d="M1 4l7 5 7-5" fill="none" stroke="var(--contact-blue)" stroke-width="1.4"/></svg>
        info@roshanbarsaz.com
      </li>
      <li>
        <svg viewBox="0 0 16 16" aria-label="Website"><circle cx="8" cy="8" r="7" fill="#fff"/><path d="M1 8h14M8 1c-3 4-3 10 0 14M8 1c3 4 3 10 0 14" fill="none" stroke="var(--contact-blue)" stroke-width="1.1"/></svg>
        www.roshanbarsaz.com
      </li>
    </ul>
  </div>
  <div class="brand-mark">
    <div class="brand-ring"></div>
    <p class="brand-name">Roshan Barsaz<br>International<br>Transport.Co L.L.c</p>
  </div>
</section>

</body>
</html>
```